Anwaltskanzlei sucht Design für Geschäftspapier, Visitenkarten, Marketing unter Einbindung des neuen Logos
Zielgruppe
Anwaltliche Rechtsberatung und Rechtsvertretung auf den Gebieten des Arbeits-, Gesellschafts- und Wirtschaftsrechts sowie des Datenschutzrechts
Zielgruppe: Mittelständische Unternehmen aller Rechtsformen und Branchen
In Kooperation mit Kanzlei Velbrand (www.kanzlei-velbrand.de)
Inhaber einer weiteren Kanzlei Velbrand & Krüger
Aufgabenstellung
Einbindung des übersandten Logos
ggf. Slogan: Kanzlei für den Mittelstand
optional: Nennung der Rechtsgebiete

```html
<!DOCTYPE html>
<html lang="de">
<head>
<meta charset="utf-8">
<title>Geschäftsbrief – Anwaltskanzlei Sterndahl</title>
<link rel="stylesheet" href="https://fonts.googleapis.com/css2?family=Arimo:wght@400&family=Open+Sans:wght@300;400;600&display=swap">
<style>
  :root {
    --backdrop: #5e6063;
    --paper: #ffffff;
    --navy: #2b2f52;
    --ink: #1e1e1e;
    --grey-text: #444444;
    --signature: #1f2a8f;
    --fold: #c9c9c9;
  }
  * { box-sizing: border-box; margin: 0; padding: 0; }
  html, body { width: 1200px; height: 945px; overflow: hidden; background: var(--backdrop); }
  .letter {
    position: absolute; left: 280px; top: 20px; width: 640px; height: 905px;
    background: var(--paper); border-top: 4px solid var(--navy);
    font-family: "Open Sans", sans-serif; color: var(--ink);
  }
  .fold-mark { position: absolute; left: 0; width: 14px; height: 1px; background: var(--fold); }
  .sender-line {
    position: absolute; left: 64px; top: 150px; font-size: 7px; color: var(--navy);
    border-bottom: 1px solid var(--navy); padding-bottom: 1px;
  }
  .sender-line strong { font-weight: 600; }
  .recipient { position: absolute; left: 64px; top: 172px; font-size: 10.5px; line-height: 1.4; }
  .recipient .city { margin-top: 9px; }
  .brand {
    position: absolute; right: 56px; top: 116px; display: flex; align-items: center; gap: 10px;
    font-weight: 300; color: var(--navy); font-size: 19px; letter-spacing: 2px; line-height: 1.05;
  }
  .brand-square { width: 14px; height: 14px; background: var(--navy); }
  .contact {
    position: absolute; right: 56px; top: 200px; width: 178px;
    border-left: 1px solid var(--navy); padding-left: 12px;
    font-size: 9px; line-height: 1.45; color: var(--ink);
  }
  .contact .firm { font-weight: 600; color: var(--navy); }
  .contact-row { display: flex; align-items: center; gap: 6px; }
  .contact-row svg { width: 8px; height: 8px; fill: var(--navy); flex: none; }
  .body-copy {
    position: absolute; left: 64px; top: 296px; width: 512px;
    font-family: "Arimo", sans-serif; font-size: 11.5px; line-height: 1.42; color: var(--ink);
  }
  .subject, .salutation, .closing, .signer { color: var(--grey-text); }
  .subject { margin-bottom: 10px; }
  .salutation { margin-bottom: 8px; }
  .body-copy p.text { text-align: justify; margin-bottom: 6px; }
  .closing { margin-top: 12px; }
  .signature { display: block; width: 150px; height: 34px; margin: 8px 0 6px;
    background: linear-gradient(90deg, rgba(31,42,143,.25), rgba(31,42,143,.12)); border-radius: 3px; }
  .footer {
    position: absolute; left: 40px; right: 40px; bottom: 40px; display: flex;
    font-size: 9px; line-height: 1.4; color: var(--ink);
  }
  .footer-col { flex: 1; padding: 0 16px; }
  .footer-col + .footer-col { border-left: 1px solid var(--ink); }
  .footer-band {
    position: absolute; left: 0; right: 0; bottom: 0; height: 28px; background: var(--navy);
    color: var(--paper); font-size: 11px; text-align: center; line-height: 28px; letter-spacing: .3px;
  }
</style>
</head>
<body>
<main class="letter">
  <span class="fold-mark" style="top:300px"></span>
  <span class="fold-mark" style="top:440px"></span>
  <span class="fold-mark" style="top:600px"></span>

  <div class="brand">
    <span class="brand-square"></span>
    <span>ANWALTSKANZLEI<br>STERNDAHL</span>
  </div>

  <p class="sender-line"><strong>Anwaltskanzlei Sterndahl</strong> | Lindenhofstraße 22 | 47809 Talheim</p>

  <address class="recipient" style="font-style:normal">
    Musterfirma<br>z. Hd. Herrn Mustermann<br>Musterweg 13
    <div class="city">24102 Musterstadt</div>
  </address>

  <address class="contact" style="font-style:normal">
    <div class="firm">Anwaltskanzlei Sterndahl</div>
    <div>Lindenhofstraße 22</div>
    <div>47809 Talheim</div>
    <div class="contact-row"><svg viewBox="0 0 10 10"><path d="M2 0h2l1 3-1.5 1a6 6 0 0 0 2.5 2.5L7 5l3 1v2a2 2 0 0 1-2 2A8 8 0 0 1 0 2a2 2 0 0 1 2-2z"/></svg>+49 2150 774120-0</div>
    <div class="contact-row"><svg viewBox="0 0 10 10"><rect x="2" y="0" width="6" height="3"/><rect x="0" y="3" width="10" height="5" rx="1"/><rect x="2" y="6" width="6" height="4"/></svg>+49 2150 774120-99</div>
    <div class="contact-row"><svg viewBox="0 0 10 10"><path d="M0 2h10v6H0z M0 2l5 3 5-3" stroke="#fff" stroke-width=".6"/></svg>info@kanzlei-sterndahl.de</div>
  </address>

  <section class="body-copy">
    <p class="subject">Betreffzeile</p>
    <p class="salutation">Sehr geehrte Damen und Herren,</p>
    <p class="text">In sollicitudin, metus et posuere blandit, erat dui bibendum eros, id vestibulum sem justo vel mauris. Ut tempor dolor ut justo vulputate, eu blandit libero faucibus. In laoreet, massa non ultricies tempor, est enim auctor mi, sit amet venenatis massa augue in justo. Praesent eu tincidunt diam. Maecenas id mi efficitur tellus interdum consectetur vel sed ante. Sed suscipit quis eros a fermentum. Curabitur ornare sit amet leo eu semper. Vestibulum pretium mi eu nisi. gadde.</p>
    <p class="text">Sed nunc est, iaculis vel enim ut, fringilla commodo lorem. Pellentesque facilisis tempus lorem eget porttitor. Morbi accumsan, nulla accumsan mollis maximus, lectus diam venenatis odio, quis bibendum elit ex a arcu. Fusce turpis erat, euismod sit amet dolor eu, hendrerit rhoncus libero. Phasellus convallis, mi vel pharetra sollicitudin, nisi purus maximus est, nec lobortis dolor enim et augue. Vestibulum auctor mi sit amet leo auctor egestas. Pellentesque eget endrerit rhoncus dan.</p>
    <p class="closing">Mit freundlichen Grüßen</p>
    <span class="signature" role="img" aria-label="Handschriftliche Unterschrift in blauer Tinte"></span>
    <p class="signer">Jonas Sterndahl</p>
  </section>

  <footer class="footer">
    <div class="footer-col">Bankverbindung:<br>Sparkasse Nordtal</div>
    <div class="footer-col">BIC: NORDDE21XXX<br>IBAN: DE12 3456 7890 1234 5678 90</div>
    <div class="footer-col">Steuernummer: 204/311/00000<br>Umsatzsteuer-ID-Nr.: DE 412097000</div>
  </footer>
  <div class="footer-band">www.kanzlei-sterndahl.de</div>
</main>
</body>
</html>
```